Property Developer - Simple yet Sophisticated and Sharp Business Card

We are a medium sized property developer involved mainly in townhouse developments and land subdivisions.

The company is looking for a simple, sharp and sophisticated business card that will be given to contractors, land owners, financiers etc and thus will need to look professional.

Property development related graphics and art can be used, however the card is not to be too "busy" or crowded. Our company name is KL Estates which could possibly be incorporated into the graphics or artwork.

Single sided and/or double sided designs will be acceptable.

A Simple, Sophisticated, Sharp design please!

Good Luck !

```html
<!DOCTYPE html>
<html lang="en">
<head>
<meta charset="utf-8">
<title>KL Estates – Business Card</title>
<link rel="stylesheet" href="https://fonts.googleapis.com/css2?family=Arimo:wght@400&display=swap">
<style>
  :root {
    --stage: #d9d9d9;
    --card: #ffffff;
    --card-shade: #f2f2f2;
    --brand-red: #c01a2c;
    --ink-grey: #5a5a5a;
    --soft-grey: #7d7d7d;
    --on-red: #ffffff;
  }
  * { margin: 0; padding: 0; box-sizing: border-box; }
  html, body {
    width: 1200px; height: 900px; overflow: hidden;
    background: var(--stage);
    font-family: "Arimo", Arial, sans-serif;
  }
  .card {
    position: absolute;
    left: 128px; top: 176px;
    width: 952px; height: 540px;
    background: linear-gradient(160deg, var(--card) 0%, var(--card) 55%, var(--card-shade) 100%);
    overflow: hidden;
  }
  .brand {
    position: absolute;
    left: 34px; top: 34px;
    display: flex; align-items: center; gap: 18px;
  }
  .brand-square {
    width: 50px; height: 50px;
    background: var(--brand-red);
  }
  .brand-name {
    font-size: 56px; font-weight: 400;
    color: var(--ink-grey);
    letter-spacing: 1px;
    line-height: 1;
  }
  .person {
    position: absolute;
    left: 0; right: 0; top: 222px;
    text-align: center;
  }
  .person-name {
    font-size: 52px; font-weight: 400;
    color: var(--brand-red);
    line-height: 1.1;
  }
  .person-role {
    font-size: 30px;
    color: var(--soft-grey);
    line-height: 1.3;
  }
  .contact-band {
    position: absolute;
    left: 0; top: 394px;
    width: 568px; height: 146px;
    background: var(--brand-red);
    color: var(--on-red);
    padding-top: 28px;
  }
  .contact-row {
    display: flex;
    font-size: 26px;
    line-height: 32px;
  }
  .contact-label { width: 80px; padding-left: 40px; box-sizing: content-box; }
  .contact-sep { width: 26px; }
  .address {
    position: absolute;
    left: 624px; top: 424px;
    font-size: 26px;
    line-height: 34px;
    color: var(--soft-grey);
  }
  .address-country { color: var(--brand-red); }
</style>
</head>
<body>
  <div class="card">
    <div class="brand">
      <div class="brand-square"></div>
      <div class="brand-name">KL Estates</div>
    </div>

    <div class="person">
      <div class="person-name">Daniel Weston</div>
      <div class="person-role">Designer</div>
    </div>

    <div class="contact-band">
      <div class="contact-row"><span class="contact-label">email</span><span class="contact-sep">:</span><span>daniel@klestates.com</span></div>
      <div class="contact-row"><span class="contact-label">tel</span><span class="contact-sep">:</span><span>+61-2-5550-0148</span></div>
      <div class="contact-row"><span class="contact-label">web</span><span class="contact-sep">:</span><span>http://www.klestates.com</span></div>
    </div>

    <div class="address">
      <div>Suite 14, 210 Harbour St,</div>
      <div>Sydney, NSW 2011</div>
      <div class="address-country">Australia</div>
    </div>
  </div>
</body>
</html>
```